Modern and Clean Photograper´s Business Card

It´s a Personal Photographer´s business card that communicates elegance, modernity, efficiency.

Target Market(s)

people that wants an efficient and qualified photographer

Industry/Entity Type

Business

Contact Information for Business Card

modern, elegant, clean

Logo Text

LuvenTor fotografia

Font styles to use
Serif
Sans Serif
Script

Colors

Designer to choose colors to be used in the design.

Requirements
Must have
• one symbol per design.
• colors that match
Nice to have
• photography simbols like shutter, camera,movement.
• blended symbols like this designs: 15160747 and 5900864
Should not have
• logo symbol too big
• colors that don´t match
• loaded of symbols, and looks like bloated.

```html
<!DOCTYPE html>
<html lang="en">
<head>
<meta charset="utf-8">
<title>LuvenTor Photographer – Business Card</title>
<link rel="stylesheet" href="https://fonts.googleapis.com/css2?family=Open+Sans:wght@400;600;700&display=swap">
<style>
  :root {
    --backdrop: #1b1b1e;
    --gold-light: #d8c9a3;
    --gold-mid: #c9b68a;
    --gold-deep: #b8a273;
    --ink: #111111;
    --card-black: #1e1e20;
    --foil: #b89667;
  }
  * { margin: 0; padding: 0; box-sizing: border-box; }
  html, body { width: 1200px; height: 800px; overflow: hidden; }
  body {
    background: var(--backdrop);
    font-family: "Open Sans", Arial, sans-serif;
    display: flex;
    align-items: center;
    justify-content: center;
    gap: 60px;
  }
  .card {
    width: 500px;
    height: 290px;
    position: relative;
    border-radius: 3px;
  }
  .card--front {
    background: linear-gradient(135deg, var(--gold-light), var(--gold-mid) 55%, var(--gold-deep));
    color: var(--ink);
  }
  .card--back {
    background: var(--card-black);
    color: var(--foil);
    display: flex;
    align-items: center;
    justify-content: center;
  }
  .identity {
    display: flex;
    align-items: center;
    gap: 18px;
  }
  .card--front .identity {
    position: absolute;
    left: 40px;
    top: 58px;
  }
  .mark {
    width: 62px;
    height: 62px;
    border-radius: 50%;
    border: 3px solid currentColor;
    flex: none;
  }
  .card--back .mark { width: 48px; height: 48px; border-width: 2px; }
  .name-block { display: flex; flex-direction: column; align-items: flex-end; }
  .name {
    font-weight: 700;
    font-size: 38px;
    letter-spacing: 1px;
    line-height: 1;
  }
  .card--back .name { font-size: 29px; font-weight: 600; }
  .role {
    font-weight: 700;
    font-size: 17px;
    margin-top: 4px;
  }
  .card--back .role { font-size: 13px; font-weight: 600; }
  .contacts {
    position: absolute;
    left: 70px;
    bottom: 38px;
    list-style: none;
    font-size: 13px;
    line-height: 21px;
  }
  .contacts li, .address {
    display: flex;
    align-items: center;
    gap: 8px;
  }
  .icon {
    width: 12px;
    height: 12px;
    background: var(--ink);
    border-radius: 2px;
    flex: none;
    display: flex;
    align-items: center;
    justify-content: center;
  }
  .icon svg { width: 9px; height: 9px; }
  .address {
    position: absolute;
    left: 300px;
    top: 180px;
    font-size: 12px;
    line-height: 15px;
    align-items: flex-start;
  }
  .address .icon { margin-top: 2px; }
</style>
</head>
<body>
  <section class="card card--front">
    <div class="identity">
      <span class="mark"></span>
      <div class="name-block">
        <span class="name">LUVENTOR</span>
        <span class="role">Photographer</span>
      </div>
    </div>

    <ul class="contacts">
      <li>
        <span class="icon"><svg viewBox="0 0 10 10"><path d="M2 1l2 2-1 1c.5 1.2 1.3 2 2.5 2.5l1-1 2 2-1.2 1.2C4.8 8.5 1.5 5.2 1 2.2z" fill="#d8c9a3"/></svg></span>
        +1 555 014 2290
      </li>
      <li>
        <span class="icon"><svg viewBox="0 0 10 10"><rect x="1" y="2.5" width="8" height="5" fill="none" stroke="#d8c9a3"/><path d="M1 2.5l4 3 4-3" fill="none" stroke="#d8c9a3"/></svg></span>
        hello@luventor.com
      </li>
      <li>
        <span class="icon"></span>
        social/luventorphoto
      </li>
      <li>
        <span class="icon"><svg viewBox="0 0 10 10"><circle cx="5" cy="5" r="3.6" fill="none" stroke="#d8c9a3"/><path d="M1.4 5h7.2M5 1.4c-1.8 2-1.8 5.2 0 7.2M5 1.4c1.8 2 1.8 5.2 0 7.2" fill="none" stroke="#d8c9a3" stroke-width=".7"/></svg></span>
        www.luventor.com
      </li>
    </ul>

    <div class="address">
      <span class="icon"><svg viewBox="0 0 10 10"><path d="M5 9C3 6.5 2 5 2 3.8a3 3 0 016 0C8 5 7 6.5 5 9z" fill="#d8c9a3"/><circle cx="5" cy="3.8" r="1" fill="#111"/></svg></span>
      <span>18 Alder Lane<br>Westbrook, ME 04092</span>
    </div>
  </section>

  <section class="card card--back">
    <div class="identity">
      <span class="mark"></span>
      <div class="name-block">
        <span class="name">LUVENTOR</span>
        <span class="role">Photographer</span>
      </div>
    </div>
  </section>
</body>
</html>
```